Portrait of a Graduate

Our school community has created a document which describes the characteristics that every student who graduates from our school should possess. We would like a visual graphic to present the information to parents\ community. We came up with three buckets (Personal, Social, and Academic) and the concept "BLH Graduates Will Be Okay" is the central theme.
We are open to 2 different concepts:
1. A ven diagram of sorts, where the three buckets are each in an area - and the over lap is "BLH Graduates Will Be Okay"
2. Our logo has a sassafras leaf in it - using the leaves to represent each bucket and the central concept as the stem - or some other creative version.

The text to be used is below:

BLH Graduates Will Be Okay (at the center/on the stem)

1. Personal
They will:
have self-worth
advocate for themselves
feel secure in their future

2. Social
They will:
embrace differences
engage in trusting relationships
be compassionate (members of their community)

3. Academic
They will:
apply skills and strategies
creatively problem-solve
achieve individual success

```html
<!DOCTYPE html>
<html lang="en">
<head>
<meta charset="utf-8">
<title>BLH Graduates Will Be Okay</title>
<link href="https://fonts.googleapis.com/css2?family=Lora:wght@400;600;700&display=swap" rel="stylesheet">
<style>
  :root {
    --navy: #1c3550;
    --green: #1d4a28;
    --orange: #f05a35;
    --yellow: #f7c531;
    --stripe-yellow: #dcb929;
    --grey: #6f6f6f;
    --paper: #ffffff;
    --backdrop: #d9d9d9;
    --leader: #b9b9b9;
  }
  * { margin: 0; padding: 0; box-sizing: border-box; }
  html, body { width: 1200px; height: 900px; overflow: hidden; }
  body {
    background: var(--backdrop);
    font-family: "Lora", Georgia, serif;
    color: var(--navy);
    position: relative;
  }
  .poster {
    position: absolute;
    left: 300px; top: 20px;
    width: 600px; height: 860px;
    background: var(--paper);
  }
  .poster-title {
    position: absolute;
    top: 162px; left: 0; width: 100%;
    text-align: center;
    font-weight: 700;
    font-size: 43px;
    line-height: 52px;
    color: var(--navy);
  }
  .pillar-diagram {
    position: absolute;
    left: 0; top: 0;
    width: 600px; height: 860px;
  }
  .pillar {
    position: absolute;
    left: 337px;
    padding-left: 12px;
    border-left: 2px solid var(--navy);
    font-size: 9.3px;
    line-height: 11px;
    color: var(--navy);
    font-weight: 600;
  }
  .pillar h2 {
    font-size: 16px;
    line-height: 18px;
    font-weight: 600;
    margin-bottom: 1px;
  }
  .pillar ul { list-style: none; }
  .pillar li::before { content: "» "; }
  .pillar--personal { top: 427px; }
  .pillar--social { top: 508px; border-color: var(--green); }
  .pillar--social h2 { color: var(--green); }
  .pillar--academic { top: 588px; border-color: var(--orange); }
  .pillar--academic h2 { color: var(--orange); }
  .school-name {
    position: absolute;
    top: 758px; left: 0; width: 100%;
    display: flex; align-items: center; justify-content: center; gap: 10px;
    font-size: 25px;
    font-weight: 400;
    color: var(--navy);
    letter-spacing: 0.5px;
  }
  .school-name .mark {
    width: 14px; height: 14px; border-radius: 50%;
    background: var(--navy);
  }
  .color-band {
    position: absolute;
    left: 0; bottom: 0; width: 100%; height: 10px;
    display: flex;
  }
  .color-band span { flex: 1; }
</style>
</head>
<body>
  <main class="poster">
    <h1 class="poster-title">BLH Graduates<br>Will Be Okay</h1>

    <svg class="pillar-diagram" viewBox="0 0 600 860" aria-hidden="true">
      <defs>
        <clipPath id="clip-personal"><circle cx="163" cy="494" r="86"/></clipPath>
        <clipPath id="clip-social"><circle cx="120" cy="583" r="88"/></clipPath>
      </defs>
      <g stroke="var(--leader)" stroke-width="0.7" stroke-dasharray="2 2">
        <line x1="172" y1="454" x2="337" y2="454"/>
        <line x1="93" y1="540" x2="337" y2="540"/>
        <line x1="172" y1="618" x2="337" y2="618"/>
      </g>
      <circle cx="163" cy="494" r="86" fill="var(--navy)"/>
      <circle cx="120" cy="583" r="88" fill="var(--green)"/>
      <circle cx="206" cy="589" r="87" fill="var(--orange)"/>
      <g clip-path="url(#clip-personal)">
        <circle cx="206" cy="589" r="87" fill="var(--navy)"/>
        <g clip-path="url(#clip-social)">
          <circle cx="206" cy="589" r="87" fill="var(--yellow)"/>
        </g>
      </g>
      <g fill="none" stroke="#fff" stroke-width="0.8" opacity="0.7">
        <g clip-path="url(#clip-personal)"><circle cx="120" cy="583" r="88"/></g>
        <g clip-path="url(#clip-social)"><circle cx="206" cy="589" r="87"/></g>
      </g>
      <circle cx="172" cy="454" r="1.6" fill="#3d8f6a"/>
      <circle cx="93" cy="540" r="1.6" fill="#4d9a45"/>
      <circle cx="172" cy="618" r="1.6" fill="#f6a23a"/>
    </svg>

    <section class="pillar pillar--personal">
      <h2>1. Personal</h2>
      <p>They will:</p>
      <ul>
        <li>have self-worth</li>
        <li>advocate for themselves</li>
        <li>feel secure in their future</li>
      </ul>
    </section>
    <section class="pillar pillar--social">
      <h2>2. Social</h2>
      <p>They will:</p>
      <ul>
        <li>embrace differences</li>
        <li>engage in trusting relationships</li>
        <li>be compassionate (members of their community)</li>
      </ul>
    </section>
    <section class="pillar pillar--academic">
      <h2>3. Academic</h2>
      <p>They will:</p>
      <ul>
        <li>apply skills and strategies</li>
        <li>creatively problem-solve</li>
        <li>achieve individual success</li>
      </ul>
    </section>

    <div class="school-name"><span class="mark"></span>Brookline Hall School</div>

    <div class="color-band">
      <span style="background: var(--navy)"></span>
      <span style="background: var(--stripe-yellow)"></span>
      <span style="background: var(--green)"></span>
      <span style="background: var(--orange)"></span>
      <span style="background: var(--grey)"></span>
    </div>
  </main>
</body>
</html>
```